Over Nine Nine Inc website design for a chic, upmarket apparel e-Commerce store

OverNine9.example is an upcoming apparel e-Commerce store that will be launched in February 2019 on Wix.com. I am seeking an original, fresh, eye-catching and classy design that is user friendly, easy to navigate and easy to check-out. It must clearly reflect the niche market we are operating in (chic fashion for petite sizes).

Details:
- Hosted at Wix.com
- Brand: Over Nine Nine (as in Over 9'9"). Logo by MarkHive attached.
- Based in Canada
- Apparel e-Commerce
- Niche segment: apparel exclusive to petite sizes (male and female)
- Website will evolve as follows:
- at launch it will have a women's shop with the following apparel categories: casual; formal; evening
- a men's section with the same categories will be added in the second phase.

Each product page will have the following information
- Product description
- 1-3 thumbnail photos per SKU. Photos should expand to full screen upon click on thumbnail
- Product description
- Available sizes
- Price
- One click addition to cart

Target Market(s)

Women and men; ages 15-40; petite size (as in short stature); should have distinct pages for casual wear, business wear, evening wear, accessories, shoes

Industry/Entity Type

Apparel Store

Coding

Coded - Design and coding required

Number of Pages Required

5+ page

Font styles to use
Serif
Sans Serif

Colors

Designer to choose colors to be used in the design.

Requirements
Must have
• Logo supplied
• Must look chic and upmarket
• Must contain a blog page
• Must contain links to our Facebook, Instagram, Twitter, LinkedIn and Pinterest pages
Should not have
• Must not be a me too design
• Do not cram too many elements in the design. Keep it minimalist, attractive and eye-catching.

```html
<!DOCTYPE html>
<html lang="en">
<head>
<meta charset="utf-8">
<title>Over Nine Nine — Summer Collection</title>
<link rel="stylesheet" href="https://fonts.googleapis.com/css2?family=Cormorant+Garamond:wght@400;500&family=Josefin+Sans:wght@300;400;600&display=swap">
<style>
  :root {
    --ink: #2b2b2b;
    --ink-soft: #6f6f6f;
    --white: #ffffff;
    --panel: #efefef;
    --rule: #d8d8d8;
    --hero-a: #9a8c83;
    --hero-b: #7d6f68;
    --banner-a: #5a4c45;
    --banner-b: #3a302c;
  }
  * { margin: 0; padding: 0; box-sizing: border-box; }
  html, body { width: 1200px; height: 3576px; overflow: hidden; }
  body {
    position: relative;
    background: var(--white);
    color: var(--ink);
    font-family: "Josefin Sans", "Helvetica Neue", Arial, sans-serif;
  }

  /* ---------- Hero ---------- */
  .hero {
    position: absolute; left: 0; top: 0; width: 1200px; height: 672px;
    background: linear-gradient(180deg, var(--hero-a), var(--hero-b));
    overflow: hidden;
  }
  .hero-photo {
    position: absolute; left: 470px; top: 40px; width: 260px; height: 632px;
    background: linear-gradient(180deg, #6c5a55 0%, #8e7f78 35%, #5c3a3f 70%, #4a2e33 100%);
    border-radius: 120px 120px 0 0;
    opacity: .85;
  }
  .hero-frame {
    position: absolute; left: 452px; top: 180px; width: 300px; height: 340px;
    border: 1px solid rgba(255,255,255,.55);
  }
  .site-header {
    position: absolute; left: 0; top: 0; width: 1200px; height: 110px;
  }
  .menu-toggle {
    position: absolute; left: 30px; top: 40px; width: 40px; height: 40px;
    border-radius: 50%; background: rgba(40,34,32,.75);
  }
  .brand {
    position: absolute; left: 0; right: 0; top: 38px; text-align: center;
    font-family: "Cormorant Garamond", Georgia, serif; font-weight: 500;
    font-size: 30px; letter-spacing: 1px; color: var(--white);
  }
  .header-tools {
    position: absolute; right: 36px; top: 48px; display: flex; gap: 22px;
  }
  .hero-title {
    position: absolute; left: 0; right: 0; top: 288px; text-align: center;
    font-weight: 300; font-size: 78px; letter-spacing: 14px; color: var(--white);
  }
  .btn-light {
    position: absolute; left: 520px; top: 448px; width: 160px; height: 34px;
    background: var(--white); color: var(--ink);
    font-size: 10px; font-weight: 600; letter-spacing: 1.5px;
    display: flex; align-items: center; justify-content: center;
  }

  /* ---------- Category rows ---------- */
  .category { position: absolute; left: 0; width: 1200px; background: var(--panel); }
  .cat-men { top: 672px; height: 676px; }
  .cat-women { top: 1348px; height: 672px; }
  .cat-kids { top: 2020px; height: 780px; }

  .feature {
    position: absolute; left: 440px; top: 0; width: 320px; background: var(--white);
    text-align: center;
  }
  .cat-men .feature { height: 648px; }
  .cat-women .feature { height: 648px; }
  .cat-kids .feature { height: 680px; }
  .feature-photo { width: 320px; height: 456px; }
  .cat-men .feature-photo { background: linear-gradient(180deg, #e4e6ea, #cfd3d8); }
  .cat-women .feature-photo { background: linear-gradient(180deg, #a48b82, #8e7670); height: 448px; }
  .cat-kids .feature-photo { background: linear-gradient(180deg, #e7e8ea, #d4d6d9); height: 448px; }
  .feature-title {
    margin-top: 52px; font-size: 20px; font-weight: 400; letter-spacing: 3px;
  }
  .feature-sub {
    margin-top: 10px; font-size: 10px; letter-spacing: 2px; color: var(--ink-soft);
  }
  .btn-outline {
    display: inline-flex; align-items: center; justify-content: center;
    margin-top: 36px; width: 136px; height: 36px;
    border: 1px solid var(--rule); font-size: 9px; font-weight: 600; letter-spacing: 1.5px;
  }

  .product {
    position: absolute; width: 240px; text-align: center;
  }
  .product-shot { width: 160px; height: 150px; margin: 0 auto; }
  .product-name {
    margin-top: 26px; font-size: 11px; letter-spacing: 2px; color: var(--ink-soft);
  }
  .product-price {
    margin-top: 8px; font-size: 11px; font-weight: 600; letter-spacing: 1px;
  }
  .col-left { left: 100px; }
  .col-right { left: 860px; }
  .row-top { top: 80px; }
  .row-bottom { top: 350px; }
  .cat-kids .row-bottom { top: 380px; }

  /* ---------- Banner ---------- */
  .story {
    position: absolute; left: 0; top: 2800px; width: 1200px; height: 480px;
    background: linear-gradient(90deg, var(--banner-b), var(--banner-a) 55%, #6b5a50);
    text-align: center; color: var(--white);
  }
  .story-mark {
    position: absolute; left: 584px; top: 40px; width: 32px; height: 32px;
    border-radius: 50%; border: 1px solid rgba(255,255,255,.7);
  }
  .story-text {
    position: absolute; left: 0; right: 0; top: 178px;
    font-weight: 300; font-size: 32px; line-height: 48px; letter-spacing: 5px;
  }

  /* ---------- Footer ---------- */
  .site-footer { position: absolute; left: 0; top: 3280px; width: 1200px; height: 296px; }
  .newsletter { position: absolute; left: 0; right: 0; top: 44px; text-align: center; }
  .newsletter-label { font-size: 10px; letter-spacing: 2px; line-height: 18px; }
  .newsletter-field {
    margin: 28px auto 0; width: 200px; height: 30px; border-bottom: 1px solid var(--rule);
    font-size: 10px; color: #a9a9a9; letter-spacing: 1px; line-height: 30px;
  }
  .btn-join {
    display: inline-flex; align-items: center; justify-content: center;
    margin-top: 22px; width: 62px; height: 28px; border: 1px solid var(--rule);
    font-size: 9px; font-weight: 600; letter-spacing: 1.5px;
  }
  .footer-bar {
    position: absolute; left: 40px; right: 40px; top: 90px; height: 20px;
    display: flex; align-items: center; justify-content: space-between;
    font-size: 9px; letter-spacing: 1.5px; color: var(--ink-soft);
  }
  .social { display: flex; gap: 14px; }
  .social span { width: 10px; height: 10px; border-radius: 50%; background: #9a9a9a; display: block; }
  .footer-nav { display: flex; gap: 40px; margin-left: 60px; }
</style>
</head>
<body>

<section class="hero">
  <div class="hero-photo" role="img" aria-label="Model in wide-brimmed hat and light grey coat over a burgundy dress"></div>
  <div class="hero-frame"></div>
  <header class="site-header">
    <div class="menu-toggle">
      <svg width="40" height="40" viewBox="0 0 40 40"><path d="M22 15l-5 5 5 5" fill="none" stroke="#fff" stroke-width="1.5"/></svg>
    </div>
    <div class="brand">Over Nine Nine</div>
    <div class="header-tools">
      <svg width="16" height="16" viewBox="0 0 16 16"><circle cx="7" cy="7" r="5" fill="none" stroke="#fff" stroke-width="1.4"/><path d="M11 11l4 4" stroke="#fff" stroke-width="1.4"/></svg>
      <svg width="16" height="16" viewBox="0 0 16 16"><rect x="2" y="5" width="12" height="10" fill="none" stroke="#fff" stroke-width="1.4"/><path d="M5 5V3.5a3 3 0 0 1 6 0V5" fill="none" stroke="#fff" stroke-width="1.4"/></svg>
    </div>
  </header>
  <h1 class="hero-title">SUMMER COLLECTION</h1>
  <a class="btn-light">BROWSE THE COLLECTION</a>
</section>

<section class="category cat-men">
  <div class="product col-left row-top">
    <div class="product-shot" role="img" aria-label="Long grey t-shirt" style="background:#5f5f5f"></div>
    <div class="product-name">LONG T-SHIRT</div><div class="product-price">£19.99</div>
  </div>
  <div class="product col-left row-bottom">
    <div class="product-shot" role="img" aria-label="Navy shorts" style="background:#2e3a52"></div>
    <div class="product-name">DERBY SHOES</div><div class="product-price">£29.99</div>
  </div>
  <div class="feature">
    <div class="feature-photo" role="img" aria-label="Man in black jacket and white shirt seated on steps"></div>
    <div class="feature-title">MANS</div>
    <div class="feature-sub">SUMMER STYLE</div>
    <a class="btn-outline">SEE ALL CLOTHING</a>
  </div>
  <div class="product col-right row-top">
    <div class="product-shot" role="img" aria-label="Olive sweatshirt" style="background:#5d6449"></div>
    <div class="product-name">SWEATSHIRT</div><div class="product-price">£7.99</div>
  </div>
  <div class="product col-right row-bottom">
    <div class="product-shot" role="img" aria-label="Beige derby shoe" style="background:#c9b6a0"></div>
    <div class="product-name">DERBY SHOES</div><div class="product-price">£29.99</div>
  </div>
</section>

<section class="category cat-women">
  <div class="product col-left row-top">
    <div class="product-shot" role="img" aria-label="Camel coat" style="background:#b98a4e"></div>
    <div class="product-name">INVITATION COAT</div><div class="product-price">£11.99</div>
  </div>
  <div class="product col-left row-bottom">
    <div class="product-shot" role="img" aria-label="Black leather court shoe" style="background:#1f1f1f"></div>
    <div class="product-name">LEATHER COURT</div><div class="product-price">£49.99</div>
  </div>
  <div class="feature">
    <div class="feature-photo" role="img" aria-label="Woman in black hat and long grey coat"></div>
    <div class="feature-title">WOMANS</div>
    <div class="feature-sub">SUMMER STYLE</div>
    <a class="btn-outline">SEE ALL CLOTHING</a>
  </div>
  <div class="product col-right row-top">
    <div class="product-shot" role="img" aria-label="Black super skinny jeans" style="background:#262626"></div>
    <div class="product-name">SUPER SKINNY</div><div class="product-price">£11.99</div>
  </div>
  <div class="product col-right row-bottom">
    <div class="product-shot" role="img" aria-label="White t-shirt" style="background:#e2e0dc"></div>
    <div class="product-name">DERBY SHOES</div><div class="product-price">£29.99</div>
  </div>
</section>

<section class="category cat-kids">
  <div class="product col-left row-top">
    <div class="product-shot" role="img" aria-label="Striped pocket t-shirt" style="background:linear-gradient(180deg,#2f3b55 50%,#9aa0aa 50%)"></div>
    <div class="product-name">T-SHIRT POCKET</div><div class="product-price">£4.99</div>
  </div>
  <div class="product col-left row-bottom">
    <div class="product-shot" role="img" aria-label="Grey sneaker" style="background:#8e9196"></div>
    <div class="product-name">DERBY SHOES</div><div class="product-price">£29.99</div>
  </div>
  <div class="feature">
    <div class="feature-photo" role="img" aria-label="Young boy in white shirt and dark trousers"></div>
    <div class="feature-title">KIDS</div>
    <div class="feature-sub">SUMMER STYLE</div>
    <a class="btn-outline">SEE ALL CLOTHING</a>
  </div>
  <div class="product col-right row-top">
    <div class="product-shot" role="img" aria-label="Black hooded jacket" style="background:#1c1c1e"></div>
    <div class="product-name">HOODED JACKET</div><div class="product-price">£7.99</div>
  </div>
  <div class="product col-right row-bottom">
    <div class="product-shot" role="img" aria-label="Denim shirt" style="background:#34486a"></div>
    <div class="product-name">DERBY SHOES</div><div class="product-price">£29.99</div>
  </div>
</section>

<section class="story" role="img" aria-label="Warm, softly lit lifestyle scene of people behind the message">
  <div class="story-mark"></div>
  <p class="story-text">DESIGNED IN NEW YORK,<br>MADE IN LOS ANGELES,<br>DELIVERED TO YOUR DOOR.</p>
</section>

<footer class="site-footer">
  <div class="newsletter">
    <div class="newsletter-label">NEWSLETTER<br>SIGN UP FOR NEWS</div>
    <div class="newsletter-field">Enter your email</div>
    <a class="btn-join">JOIN</a>
  </div>
  <div class="footer-bar">
    <div class="social"><span></span><span></span><span></span><span></span><span></span></div>
    <nav class="footer-nav"><span>ABOUT US</span><span>STORE LOCATOR</span><span>CONTACT</span><span>TERMS</span><span>BLOG</span></nav>
    <div class="copyright">COPYRIGHT 2019</div>
  </div>
</footer>

</body>
</html>
```